Keystone Facility Partners Business card

We wish to have a professional Business card to present to large Corporate CEO's ASAP.

Our web site helps explain our business www.keystonefp.org

Keystone Facility Partners was established after we discovered how difficult it is to organise outsourced services while heading up a business or company.

We act as a facilitator for businesses who don't have the desire, expertise or recourses to manage their own systems and meet all their requirements.

We provide an all in one facility management solution for all types of businesses. We manage schedules, contractors and costs on behalf of businesses and their needs and wants.

Having an extensive network ensures we are able to connect businesses with the right service providers.

Target Market(s)

Company CEO

Industry/Entity Type

Business

Font styles to use
Sans Serif

Colors
33a6d7
f9fdfe
0355a3

Requirements
Must have
• professional design
Nice to have
• colours to match logo

```html
<!DOCTYPE html>
<html lang="en">
<head>
<meta charset="utf-8">
<title>Keystone Facility Partners — Business Card</title>
<link rel="stylesheet" href="https://fonts.googleapis.com/css2?family=Arimo:wght@400;700&display=swap">
<style>
  :root {
    --sky: #33a6d7;
    --paper: #f9fdfe;
    --navy: #0355a3;
    --ink: #151515;
    --mist: #dfe4f3;
    --link-blue: #1d63b8;
    --backdrop: #eceff3;
  }
  * { box-sizing: border-box; margin: 0; padding: 0; }
  html, body {
    width: 1200px;
    height: 900px;
    overflow: hidden;
    background: var(--backdrop);
    font-family: "Arimo", Arial, sans-serif;
  }
  .card {
    position: absolute;
    left: 100px;
    top: 170px;
    width: 1000px;
    height: 560px;
    background: var(--mist);
    border: 10px solid #e8ecf8;
    box-shadow: 0 6px 18px rgba(0,0,0,0.18);
    overflow: hidden;
  }
  .brand-panel {
    position: absolute;
    left: 0; top: 0;
    width: 980px;
    height: 298px;
    background: var(--paper);
  }
  .brand {
    position: absolute;
    left: 50px;
    top: 84px;
    display: flex;
    align-items: center;
    gap: 30px;
  }
  .brand-dot {
    width: 130px;
    height: 130px;
    border-radius: 50%;
    background: var(--navy);
  }
  .brand-name {
    font-weight: 700;
    font-size: 54px;
    color: var(--ink);
    letter-spacing: 0.5px;
  }
  .waves {
    position: absolute;
    left: 0; top: 0;
    width: 980px;
    height: 540px;
  }
  .contact {
    position: absolute;
    left: 22px;
    top: 320px;
    color: var(--link-blue);
    line-height: 1.12;
    white-space: nowrap;
  }
  .contact-name { font-size: 33px; }
  .contact-line { font-size: 35px; }
  .contact-email { font-size: 30px; }
  .services {
    position: absolute;
    left: 545px;
    top: 330px;
    color: var(--ink);
    white-space: nowrap;
  }
  .services-title { font-size: 20px; margin-bottom: 6px; }
  .services-list { list-style: none; font-size: 14px; line-height: 1.65; }
  .services-list li::before,
  .provision::before {
    content: "";
    display: inline-block;
    width: 9px; height: 9px;
    border-radius: 50%;
    background: var(--navy);
    margin-right: 8px;
    vertical-align: 1px;
  }
  .provision-block {
    position: absolute;
    left: 22px;
    top: 464px;
    line-height: 1.2;
    white-space: nowrap;
  }
  .provision { font-size: 15px; color: var(--ink); }
  .trades { font-size: 14px; color: var(--link-blue); padding-left: 17px; }
</style>
</head>
<body>
  <div class="card">
    <div class="brand-panel">
      <div class="brand">
        <div class="brand-dot"></div>
        <div class="brand-name">Keystone Facility Partners</div>
      </div>
    </div>

    <svg class="waves" viewBox="0 0 980 540" aria-hidden="true">
      <line x1="0" y1="303" x2="980" y2="303" stroke="var(--navy)" stroke-width="6"/>
      <path d="M0 442 C 300 442, 430 436, 480 386 C 530 330, 650 314, 980 298 L 980 312 C 660 328, 560 342, 505 400 C 455 454, 300 458, 0 458 Z" fill="var(--sky)"/>
    </svg>

    <div class="contact">
      <div class="contact-name">Daniel Whitford</div>
      <div class="contact-line">Contact : 0412 555 018</div>
      <div class="contact-email">Email: daniel@keystonefp.org</div>
    </div>

    <div class="services">
      <div class="services-title">Our range of services includes:</div>
      <ul class="services-list">
        <li>Auditing process of all current services</li>
        <li>Contract Management of all current services</li>
        <li>Risk Management services</li>
        <li>Hospitality and Event Management</li>
        <li>Secure documentation destruction</li>
        <li>Providing a technology platform to manage facility requirements</li>
      </ul>
    </div>

    <div class="provision-block">
      <div class="provision">Direct service provision for all facility management services</div>
      <div class="trades">Cleaning, Waste Management, Security, Electrical, Fire</div>
      <div class="trades">General Building Maintenance, Plumbing, Pest Control</div>
      <div class="trades">Yard and Garden Maintenance</div>
    </div>
  </div>
</body>
</html>
```